4 x 9 Rack Card Design: Cheer Every Game Advertising Campaign

We would like a 4 x 9 Rack Card Designed using our logo as the basis for the design. We would like to incorporate the images of the shoes & the colors that are on our logo. We are attaching an image of the logo for your use.

The design should use both the front & back of the 4 x 9 card.

All text & fonts should be in "comic sans".

The card should have a fun, youthful, cartoon feel to it.

We would like the following information on the card:
Our logo: See attached file

Our Tag Line: Charity providing Athletic Footwear to Kids

Our Catch Phrase: "Cheer Every Game". Please include small images of various sports balls under, or around or near the catch phrase. Please use images of a Basketball, baseball, golf ball, soccer ball, Hockey Puck, American Football, Tennis ball.

Our Contact Information: PO Box 30628, Phoenix, AZ 85019; phone 480.213.4496; www.brightlace-kids.org; also use the "find us on linkwall" image.

Who we are: We are a 501(c)3 non-profit organization providing athletic footwear to disadvantaged and at-risk youth. The proper footwear allows participation in sports activities providing a healthy outlet for energy, increased self confidence, reduced juvenile crime rates, decline in alcohol, tobacco and drug dependency, strengthened relationships and enhanced academic performance.

A Recipe: We are working on a recipe to be included. In the meantime, we are asking for designs that include a small area for a recipe on the back of the card. The recipe will be easy, with very few ingredients & instructions, so it won't take up too much space on the rack card.

Target Market(s)

Sponsors, endorsers, donators, sports teams.

Industry/Entity Type

Non-Profit

Font styles to use
Other font styles liked:
• Comic Sans

Requirements
Must have
• See project descripion
Nice to have
• See project description. Also, please take a look at our website at www.brightlace-kids.com for our style & additional information about our organization.

```html
<!DOCTYPE html>
<html lang="en">
<head>
<meta charset="utf-8">
<title>Brightlace Kids – Rack Card</title>
<link rel="stylesheet" href="https://fonts.googleapis.com/css2?family=Comic+Neue:wght@400;700&display=swap">
<style>
:root{
  --pink:#e2498a;
  --blue:#1e9ad6;
  --green:#8cc63f;
  --green-dark:#5e9a22;
  --ink:#2b2b2b;
  --sky:#dcebf6;
  --field:#e8cf3e;
  --field-deep:#c9a92a;
  --sunset:#f3b567;
  --stage:#d9d9d9;
}
*{box-sizing:border-box;margin:0;padding:0}
html,body{width:1200px;height:825px;overflow:hidden}
body{background:var(--stage);position:relative;font-family:"Comic Neue",cursive;color:var(--ink)}
.card{position:absolute;top:44px;width:329px;height:738px;overflow:hidden;background:linear-gradient(#cfe3f3 0%,#f4f8fb 45%,#ffffff 100%)}
.card--front{left:241px}
.card--back{left:628px}
.abs{position:absolute}
.shape{position:absolute;left:0;top:0}
.photo{position:absolute}
.photo-circle{position:absolute;border-radius:50%;border:5px solid var(--blue);background:#fff}
.photo-circle .photo{inset:3px;border-radius:50%}
.photo-circle--pink{border-color:var(--pink)}
.badge{position:absolute;border-radius:50%;background:#fff;display:flex;flex-direction:column;align-items:center;justify-content:center;text-align:center;font-weight:700;line-height:1.2;font-size:14px}
.badge--green{border:5px solid var(--green)}
.badge--blue{border:5px solid var(--blue)}
.c-blue{color:var(--blue)}
.c-pink{color:var(--pink)}
.c-ink{color:var(--ink)}
.brand-name{position:absolute;left:0;width:100%;text-align:center;font-weight:700;font-size:34px;color:var(--blue);letter-spacing:1px}
.url-band{position:absolute;left:0;bottom:0;width:100%;height:30px;display:flex;align-items:center;justify-content:center;font-size:17px;font-weight:700;letter-spacing:2px}
/* front */
.tagline{left:0;top:320px;width:100%;text-align:center;font-weight:700;font-size:21px;color:#3a3a3a}
.tagline-accent{left:0;top:346px;width:100%;text-align:center;font-weight:700;font-size:31px;color:var(--pink)}
.catch{left:48px;top:398px;width:270px;text-align:center;font-weight:700;font-size:25px;color:var(--ink)}
.url-band--blue{background:var(--blue);color:#fff}
/* back */
.about{left:24px;top:166px;width:282px;font-size:10.6px;line-height:1.24;text-align:justify;color:#333}
.recipe-title{left:0;top:394px;width:100%;text-align:center;font-size:21px;font-weight:700;color:var(--blue)}
.recipe-text{left:24px;top:420px;width:282px;font-size:10.4px;line-height:1.24;text-align:justify;color:#333}
.contact{left:0;top:594px;width:100%;text-align:center;font-weight:700;font-size:13.5px;line-height:17px}
.social{left:0;top:656px;width:100%;display:flex;justify-content:center;gap:20px;font-weight:700;font-size:14px;align-items:center}
.social-item{display:flex;align-items:center;gap:6px}
.social-dot{width:26px;height:26px;border-radius:50%;background:var(--pink)}
.url-band--green{background:var(--green);color:#333}
</style>
</head>
<body>

<section class="card card--front" aria-label="Rack card front">
  <div class="photo" role="img" aria-label="Photo of a runner's feet in pink sneakers on a road at sunset"
       style="left:0;top:0;width:329px;height:262px;background:linear-gradient(170deg,#f6d6a8 0%,var(--sunset) 40%,#b86c3c 70%,#3b2f2b 100%);clip-path:polygon(0 0,100% 0,100% 212px,52% 258px,0 212px)"></div>
  <svg class="shape" width="329" height="300" viewBox="0 0 329 300" aria-hidden="true">
    <polygon points="0,212 171,258 329,212 329,224 171,271 0,224" fill="var(--pink)"/>
    <polygon points="0,224 171,271 329,224 329,229 171,276 0,229" fill="#ffffff"/>
  </svg>
  <div class="badge badge--green" style="left:125px;top:215px;width:92px;height:92px">
    <span class="c-blue">Brightlace</span><span class="c-ink">Kids</span><span class="c-blue">Charity</span>
  </div>

  <p class="abs tagline">Charity providing Athletic</p>
  <p class="abs tagline-accent">Footwear to Kids</p>

  <svg class="shape" style="top:394px" width="329" height="48" viewBox="0 0 329 48" aria-hidden="true">
    <polygon points="22,2 329,2 329,42 34,42" fill="var(--green)"/>
    <polygon points="22,2 34,42 30,46 18,8" fill="var(--green-dark)"/>
  </svg>
  <p class="abs catch">Cheer Every Game</p>

  <p class="brand-name" style="top:505px">Brightlace Kids</p>

  <div class="photo" role="img" aria-label="Photo of a sunlit grass field at sunset"
       style="left:0;top:560px;width:329px;height:140px;background:linear-gradient(#f5c765 0%,var(--field) 45%,var(--field-deep) 100%)"></div>
  <div class="photo-circle" style="left:29px;top:596px;width:70px;height:70px">
    <div class="photo" role="img" aria-label="Photo of children's legs in sneakers" style="background:linear-gradient(#9fc7e6,#d7c3a8)"></div>
  </div>
  <div class="photo-circle photo-circle--pink" style="left:123px;top:583px;width:96px;height:96px">
    <div class="photo" role="img" aria-label="Photo of a foot resting on a soccer ball" style="background:radial-gradient(circle at 50% 65%,#f2f2f2 0 30%,#7a5a45 60%,#3d3a36 100%)"></div>
  </div>
  <div class="photo-circle" style="left:231px;top:593px;width:76px;height:76px">
    <div class="photo" role="img" aria-label="Photo of a child walking on a green in sneakers" style="background:linear-gradient(#cfe2ef,#6fae4f)"></div>
  </div>

  <svg class="shape" style="top:698px" width="329" height="12" viewBox="0 0 329 12" aria-hidden="true">
    <rect x="0" y="2" width="329" height="2" fill="var(--pink)"/>
    <rect x="0" y="6" width="329" height="3" fill="#ffffff"/>
  </svg>
  <div class="url-band url-band--blue">www.brightlace-kids.org</div>
</section>

<section class="card card--back" aria-label="Rack card back">
  <div class="photo" role="img" aria-label="Photo of sky over a golden grass field"
       style="left:0;top:250px;width:330px;height:330px;background:linear-gradient(rgba(255,255,255,0) 0%,#dfe9c6 30%,var(--field) 60%,var(--field-deep) 100%)"></div>

  <p class="brand-name" style="top:88px">Brightlace Kids</p>

  <p class="abs about">We are a 501(c)3 non-profit organization providing athletic footwear to disadvantaged and at-risk youth. The proper footwear allows participation in sports activities providing a healthy outlet for energy, increased self confidence, reduced juvenile crime rates, decline in alcohol, tobacco and drug dependency, strengthened relationships and enhanced academic performance.</p>

  <div class="photo-circle" style="left:29px;top:294px;width:80px;height:80px">
    <div class="photo" role="img" aria-label="Photo of a hiking shoe on rock" style="background:linear-gradient(#b88a66,#4d6f8f)"></div>
  </div>
  <div class="photo-circle photo-circle--pink" style="left:119px;top:286px;width:96px;height:96px">
    <div class="photo" role="img" aria-label="Photo of children's legs on a putting green" style="background:linear-gradient(#f1eee8,#88b566)"></div>
  </div>
  <div class="photo-circle" style="left:231px;top:294px;width:80px;height:80px">
    <div class="photo" role="img" aria-label="Photo of a kick at a soccer ball on grass" style="background:linear-gradient(#9cc5e6,#5f9a45)"></div>
  </div>

  <p class="abs recipe-title">A Recipe:</p>
  <p class="abs recipe-text">Lorem ipsum dolor sit amet, consectetuer adipiscing elit, sed diam nonummy nibh euismod tincidunt ut laoreet dolore magna aliquam erat volutpat.consectetuer adipiscing elit, sed diam nonummy nibh euismod tincidunt ut laoreet.</p>

  <svg class="shape" width="330" height="738" viewBox="0 0 330 738" aria-hidden="true">
    <polygon points="0,562 166,500 330,580 330,738 0,738" fill="var(--pink)"/>
    <polygon points="0,572 166,510 330,590 330,738 0,738" fill="#ffffff"/>
  </svg>
  <div class="badge badge--blue" style="left:116px;top:482px;width:100px;height:100px">
    <span class="c-pink">Brightlace</span><span class="c-ink">Kids</span><span class="c-pink">Charity</span>
  </div>

  <div class="abs contact">
    <p class="c-ink">PO Box 30628, Phoenix, AZ 85019</p>
    <p class="c-blue">Phone 480.213.4496</p>
    <p class="c-ink">Visit: www.brightlace-kids.org</p>
  </div>
  <div class="abs social">
    <span class="social-item">Like us on: <span class="c-pink">linkwall</span><span class="social-dot"></span></span>
    <span class="social-item">Follow us on: <span class="c-pink">chirpline</span><span class="social-dot"></span></span>
  </div>

  <svg class="shape" style="top:695px" width="330" height="6" viewBox="0 0 330 6" aria-hidden="true">
    <rect x="0" y="1" width="330" height="3" fill="var(--pink)"/>
  </svg>
  <div class="url-band url-band--green">www.brightlace-kids.org</div>
</section>

</body>
</html>
```